Alcohol/Drug addiction treatment center and detox facility needs a billboard.

We are a new treatment center in Auburn, IN (2020), specializing in helping folks who are struggling with alcohol/drug addiction. We offer medical detox, inpatient, and outpatient care in a beautiful, safe, and stable environment, where patients will detox comfortably and then learn the coping skills necessary to lead a successful, sober life. The ad should reach people on a personal/emotional level - addicts who are overwhelmed as well as their families - reminding them that the tentacles of addiction are far-reaching; further, it should convey that you are not alone, we are committed to helping you learn how to lead a successful life, and we are here 24/7/365.
Updates

Here are some slogans that are popular in the treatment industry right now: -Your baby’s life shouldn’t begin with 1-866-HEAL-NOW (Maybe use our phone number as the last word) -Treatment Changes Everything. -Brookmere turns fear into Hope. -Pain killers are easy to get into hard to escape -It only takes a little to lose a lot. -Alcohol, Herion, Pills it all kills. -Loved one hooked on Herion? Brookmere ect. -Drive Hammered get nailed -Recovery is real -Brookmere turns fear into hope.

Target Market(s)

People struggling with addiction and their families.

Industry/Entity Type

Addiction Treatment centers

Colors

Designer to choose colors to be used in the design.

Requirements
Must have
• Brookmere Treatment; 866-HEAL-NOW; www.brookmeretreatment.example
Nice to have
• Catchy slogan - Examples: 1. Your baby’s life shouldn’t begin with 1-866-HEAL-Now (we could use our phone number for the last word) 2. Treatment Changes Everything. 3. It only takes a little to lose a lot. 4. Alcohol, Heroin, Pills it all kills. 5. Loved one hooked on Heroin? Brookmere can help. 6. Drive Hammered get nailed 7. Recovery is real 8. Brookmere turns fear into hope. 9. Pain killers are easy to get into hard to escape

```html
<!DOCTYPE html>
<html lang="en">
<head>
<meta charset="utf-8">
<title>Brookmere Treatment — Billboard</title>
<link rel="stylesheet" href="https://fonts.googleapis.com/css2?family=Jost:wght@500;600&display=swap">
<style>
  :root {
    --backdrop: #82afc4;
    --navy: #20295a;
    --white: #ffffff;
    --cyan: #27c0ee;
  }
  * { box-sizing: border-box; margin: 0; padding: 0; }
  html, body {
    width: 1200px;
    height: 1052px;
    overflow: hidden;
    background: var(--backdrop);
    font-family: "Jost", "Futura", sans-serif;
  }
  .billboard {
    position: absolute;
    left: 49px;
    top: 361px;
    width: 1094px;
    height: 330px;
    display: flex;
  }
  .message-panel {
    position: relative;
    width: 734px;
    height: 100%;
    background: var(--navy);
    color: var(--white);
    overflow: hidden;
  }
  .headline,
  .support-line,
  .phone {
    position: absolute;
    left: 35px;
    line-height: 1;
    white-space: nowrap;
  }
  .headline {
    top: 60px;
    font-size: 72px;
    font-weight: 600;
    letter-spacing: 0.5px;
  }
  .support-line {
    top: 190px;
    font-size: 42px;
    font-weight: 500;
  }
  .phone {
    top: 242px;
    font-size: 48px;
    font-weight: 500;
    color: var(--cyan);
  }
  .brand-panel {
    position: relative;
    flex: 1;
    height: 100%;
    background: var(--white);
    display: flex;
    flex-direction: column;
    align-items: center;
    padding-top: 52px;
  }
  .brand-dot {
    width: 130px;
    height: 130px;
    border-radius: 50%;
    background: var(--cyan);
  }
  .brand-name {
    margin-top: 36px;
    font-size: 30px;
    font-weight: 500;
    color: var(--navy);
    line-height: 1;
    white-space: nowrap;
  }
  .website {
    margin-top: 16px;
    font-size: 15px;
    font-weight: 500;
    letter-spacing: 1px;
    color: var(--cyan);
    line-height: 1;
    white-space: nowrap;
  }
</style>
</head>
<body>
  <main class="billboard">
    <section class="message-panel">
      <h1 class="headline">Do you need drugs?</h1>
      <p class="support-line">We can help you:</p>
      <p class="phone">1-866-HEAL-NOW</p>
    </section>
    <section class="brand-panel">
      <span class="brand-dot" aria-hidden="true"></span>
      <p class="brand-name">Brookmere Treatment</p>
      <p class="website">www.brookmeretreatment.example</p>
    </section>
  </main>
</body>
</html>
```